Larkmoor Blind Company / Blind Sale postcard mailer

I need a Design for a two sided postcard, advertising products for our company. One side will mainly show blinds & shutters, and the "call out" will be "Blind Sale / $59.99 per window". Then a place underneath for details. The other side of the card can showcase our other products (shades, exterior, etc). I would like the overall look and feel of the card to resemble the website design and colors, etc, you see at www.quillstonehome.example and www.fernwickdecor.example. You can use any images from my Stashbin page here: https://www.stashbin.example/sh/4kdmq8rtzvewplx/QQT2HHjbWpaLm731gxJtRsZ?dl=0

Use images from the Birchwave folder in Stashbin.
Also, my website for reference is www.larkmoorblinds.example
Larkmoor Blind Company

The printed card will be very plastic, heavy glossy. Heavier than most. I want the card to be as striking as possible, harder for customer to throw away. Trying to avoid lots of clutter on the card. Custom Template attached.

Target Market(s)

Card will be targeted mainly to new homeowners, especially new construction homes

Industry/Entity Type

It Company

Font styles to use
Serif
Sans Serif

Requirements
Must have
• Clean, uncluttered look. Best looking images. Logo somewhere on card. Open to changing the color of logo (i.e., if whites and greys are the main color, could do a white and grey version of logo..)

```html
<!DOCTYPE html>
<html lang="en">
<head>
<meta charset="utf-8">
<title>Larkmoor Blind Company – Blind Sale Postcard</title>
<link href="https://fonts.googleapis.com/css2?family=Oswald:wght@600;700&family=Open+Sans:wght@400;600;700;800&display=swap" rel="stylesheet">
<style>
  :root{
    --red:#c8141b;
    --red-dark:#a20f15;
    --navy:#1c2f6b;
    --navy-deep:#13224f;
    --navy-light:#2b4a8f;
    --ink:#1a1a1a;
    --white:#ffffff;
    --paper:#f1f1f1;
    --bg:#e4e4e4;
  }
  *{box-sizing:border-box;margin:0;padding:0}
  html,body{width:900px;height:1200px;overflow:hidden}
  body{background:var(--bg);font-family:"Open Sans",Arial,sans-serif;position:relative;color:var(--ink)}

  .card{position:absolute;left:70px;width:760px;height:372px;background:var(--white);overflow:hidden;box-shadow:0 6px 18px rgba(0,0,0,.18)}
  .card-front{top:155px}
  .card-back{top:668px;height:370px;width:758px}

  /* brand */
  .brand{position:absolute;display:flex;align-items:center;gap:5px}
  .brand-mark{width:10px;height:10px;background:var(--navy-light);flex:none}
  .brand-name{font-family:"Open Sans",Arial,sans-serif;font-weight:700;font-size:7.5px;line-height:10px;color:var(--navy);text-transform:uppercase;letter-spacing:.2px}

  /* front */
  .front-header{position:absolute;left:0;top:0;width:100%;height:80px;background:linear-gradient(#ffffff,#ebebeb)}
  .front-header .brand{left:28px;top:22px}
  .sale-title{position:absolute;left:127px;top:10px;font-family:"Oswald",Impact,sans-serif;font-weight:700;font-size:60px;line-height:64px;color:var(--red);letter-spacing:-.5px}
  .sale-price{position:absolute;left:445px;top:28px;font-family:"Open Sans",Arial,sans-serif;font-weight:800;font-size:30px;line-height:36px;color:var(--navy)}
  .sale-price span{color:var(--ink);font-weight:700;font-size:24px;margin-left:4px}
  .photo-band{position:absolute;left:0;top:80px;width:760px;height:188px}
  .front-footer{position:absolute;left:0;top:265px;width:100%;height:107px;background:linear-gradient(90deg,var(--navy-deep),var(--navy-light) 50%,var(--navy-deep))}
  .feature{position:absolute;top:14px;width:330px;color:var(--white)}
  .feature h2{font-family:"Open Sans",Arial,sans-serif;font-weight:800;font-size:19px;line-height:24px;text-transform:uppercase}
  .feature p{font-size:8px;line-height:11px;margin-top:4px}
  .feature-blinds{left:30px;text-align:justify}
  .feature-shutters{right:38px;text-align:right}
  .feature-divider{position:absolute;left:385px;top:22px;width:1px;height:55px;background:rgba(255,255,255,.35)}

  /* back */
  .back-panel{position:absolute;left:0;top:0;width:470px;height:370px;background:linear-gradient(#ffffff,#e6e6e6)}
  .card-back .brand{left:20px;top:26px}
  .back-title{position:absolute;left:86px;top:30px;color:var(--navy);white-space:nowrap}
  .back-title h1{font-family:"Open Sans",Arial,sans-serif;font-weight:800;font-size:18px;line-height:21px;text-transform:uppercase}
  .back-title p{font-weight:700;font-size:10.5px;line-height:14px;text-transform:uppercase;color:#333}
  .back-intro{position:absolute;left:18px;top:80px;width:262px;text-align:center;font-weight:700;font-size:10px;line-height:14px;color:#333;white-space:nowrap}
  .product{position:absolute;left:0}
  .product-tag{display:inline-block;width:95px;height:22px;background:var(--navy);color:var(--white);border-radius:0 11px 11px 0;font-weight:800;font-size:12px;line-height:22px;padding-left:23px;text-transform:uppercase}
  .product p{font-size:7.5px;line-height:11px;padding:5px 0 0 18px;color:#222}
  .product-shades{top:115px;width:262px}
  .product-exterior{top:198px;width:250px}
  .contact{position:absolute;left:0;top:284px;width:300px;height:86px}
  .contact-list{position:absolute;left:24px;top:292px;list-style:none;color:var(--white)}
  .contact-list li{display:flex;align-items:center;gap:8px;font-weight:600;font-size:17px;line-height:22px}
  .contact-list li.email{font-size:11px;line-height:22px}
  .contact-list svg{width:11px;height:11px;flex:none}
  .photo-stack{position:absolute;left:220px;top:0;width:250px;height:370px}
  .stamp-box{position:absolute;left:661px;top:22px;width:64px;height:58px;border:1px solid #555}
  .address-line{position:absolute;left:480px;width:200px;height:2px;background:#888}
</style>
</head>
<body>

<section class="card card-front" aria-label="Postcard front">
  <header class="front-header">
    <div class="brand"><span class="brand-mark"></span><span class="brand-name">Larkmoor<br>Blind<br>Company</span></div>
    <div class="sale-title">BLIND SALE</div>
    <div class="sale-price">$59.99<span>per window</span></div>
  </header>

  <svg class="photo-band" viewBox="0 0 760 188">
    <defs>
      <linearGradient id="roomWarm" x1="0" y1="0" x2="1" y2="1">
        <stop offset="0" stop-color="#c9a56a"/><stop offset=".5" stop-color="#8a6a48"/><stop offset="1" stop-color="#4a3a32"/>
      </linearGradient>
      <linearGradient id="roomDusk" x1="0" y1="0" x2="1" y2="1">
        <stop offset="0" stop-color="#5a5048"/><stop offset=".5" stop-color="#8b6e52"/><stop offset="1" stop-color="#b88e5e"/>
      </linearGradient>
    </defs>
    <rect x="0" y="0" width="760" height="188" fill="var(--red)"/>
    <rect x="0" y="5" width="375" height="176" fill="url(#roomWarm)" role="img" aria-label="Living room with wood blinds"/>
    <rect x="382" y="5" width="378" height="176" fill="url(#roomDusk)" role="img" aria-label="Dining and sitting room with plantation shutters"/>
    <polygon points="118,181 130,181 225,5 213,5" fill="var(--red)"/>
    <polygon points="140,181 145,181 240,5 235,5" fill="var(--red)"/>
    <polygon points="470,181 482,181 575,5 563,5" fill="var(--red)"/>
    <polygon points="490,181 495,181 590,5 585,5" fill="var(--red)"/>
    <path d="M0 150 Q40 172 110 181 L0 181 Z" fill="var(--red)"/>
    <rect x="0" y="181" width="760" height="7" fill="var(--red)"/>
  </svg>

  <footer class="front-footer">
    <div class="feature feature-blinds">
      <h2>Blinds</h2>
      <p>Wood Blinds are a versatile custom window treatment that can work beautifully in any window. Manufactured from a variety of North American hardwoods, the detailed finishing process for our wood blinds provides long-lasting protection against daily wear, including fading, scratches, and moisture.</p>
    </div>
    <span class="feature-divider"></span>
    <div class="feature feature-shutters">
      <h2>Shutters</h2>
      <p>Shutters are a great decorating choice for many reasons. From a design viewpoint, they easily blend with the architectural elements of most windows, and can compliment both traditional and contemporary styles.</p>
    </div>
  </footer>
</section>

<section class="card card-back" aria-label="Postcard back">
  <div class="back-panel"></div>
  <div class="brand"><span class="brand-mark"></span><span class="brand-name">Larkmoor<br>Blind<br>Company</span></div>
  <div class="back-title">
    <h1>The Finest Window</h1>
    <p>Treatment Products Available</p>
  </div>
  <p class="back-intro">we provide our clientele with the perfect combination<br>of selection, quality, and value, all enhanced</p>

  <div class="product product-shades">
    <span class="product-tag">Shades</span>
    <p>Cellular shades are a clean, elegant and functional solution for your windows. Available in a variety of blackout and translucent fabrics which are made with crisp pleats, the shade cells create a “honeycomb” shape, thus trapping the air.</p>
  </div>
  <div class="product product-exterior">
    <span class="product-tag">Exterior</span>
    <p>Exterior Solar Shades are an affordable and stylish solution for privacy and sun control for outdoor living spaces, such as porches and decks. The shades will filter and diffuse light, while maintaining an outward view.</p>
  </div>

  <svg class="contact" viewBox="0 0 300 86" preserveAspectRatio="none" aria-hidden="true">
    <defs>
      <linearGradient id="navyBand" x1="0" y1="0" x2="1" y2="0">
        <stop offset="0" stop-color="var(--navy-deep)"/><stop offset="1" stop-color="var(--navy-light)"/>
      </linearGradient>
    </defs>
    <polygon points="0,0 300,0 255,86 0,86" fill="url(#navyBand)"/>
  </svg>
  <ul class="contact-list">
    <li><svg viewBox="0 0 12 12"><rect x="1" y="1" width="10" height="10" rx="2" fill="#fff"/><path d="M4 3 L5 3 L5.5 5 L4.8 5.6 Q5.6 7 6.6 7.4 L7.2 6.6 L9 7.2 L9 8.3 Q6 8.8 3.6 4.2 Z" fill="var(--navy)"/></svg>555-210-4837</li>
    <li><svg viewBox="0 0 12 12"><rect x="3" y="1" width="6" height="3" fill="#fff"/><rect x="1" y="4" width="10" height="5" rx="1" fill="#fff"/><rect x="3" y="8" width="6" height="3" fill="#fff" stroke="var(--navy)" stroke-width=".6"/></svg>555-210-4838</li>
    <li class="email"><svg viewBox="0 0 12 12"><circle cx="6" cy="6" r="5" fill="#fff"/><path d="M1 6 H11 M6 1 Q3 6 6 11 Q9 6 6 1" stroke="var(--navy)" stroke-width=".7" fill="none"/></svg>info@larkmoorblinds.example</li>
  </ul>

  <svg class="photo-stack" viewBox="0 0 250 370">
    <defs>
      <linearGradient id="sunroom" x1="0" y1="0" x2="1" y2="1"><stop offset="0" stop-color="#d9d6cf"/><stop offset="1" stop-color="#6b5a4a"/></linearGradient>
      <linearGradient id="den" x1="0" y1="0" x2="1" y2="1"><stop offset="0" stop-color="#a88058"/><stop offset="1" stop-color="#5b4a3e"/></linearGradient>
      <linearGradient id="porch" x1="0" y1="0" x2="1" y2="1"><stop offset="0" stop-color="#6b4b33"/><stop offset="1" stop-color="#d8d0c2"/></linearGradient>
    </defs>
    <polygon points="93,0 245,0 155,370 0,370" fill="var(--red)"/>
    <polygon points="103,15 225,15 198,122 103,122" fill="url(#sunroom)" role="img" aria-label="Sunroom dining area with cellular shades"/>
    <polygon points="60,132 193,132 166,237 60,237" fill="url(#den)" role="img" aria-label="Family room with shaded windows"/>
    <polygon points="23,249 162,249 137,354 23,354" fill="url(#porch)" role="img" aria-label="Porch with exterior solar shade"/>
  </svg>

  <span class="stamp-box"></span>
  <span class="address-line" style="top:208px"></span>
  <span class="address-line" style="top:240px"></span>
  <span class="address-line" style="top:273px"></span>
</section>

</body>
</html>
```